Modify mobile web Photoshop design to make them look great

We need to choose and refine the stock image to look great on 5 mobile web pages: 1) Hourglass image on home screen, 2) Sofa image on registration screen, 3) Loveseat image on login screen, 4) Lamp for reminder screen, and 5) Bed for ratings / score screen. Sample photos denote what customer wants, but they are just downloaded from Brindo, and is not purchased stock photos. Designers need to show that the updated photos used are properly purchased from stock photo source. Photoshop files for all 5 mobile web pages are provided. Artists are requested to edit and submit the 5 photoshop files and make them look as good as possible with the constraints above. No change is needed on the layout or anything beside the 5 stock images, but subtle refinements are OK if you believe it would improve the overall design without affecting the art direction.

Target Market(s)

Travel, Lifestyle

Industry/Entity Type

Hospitality

Font styles to use
Sans Serif

Requirements
Must have
• Stock photos must be properly licensed, artists must put updated stock photos back into supplied photoshop source files, updated look and feel should have the same general art direction, images must be hourglass, sofa, loveseat, lamp and bed
Nice to have
• Minor and very subtle touchup of other elements without affecting any design work of the layout such as color scheme
Should not have
• Should not affect art direction, identity and color of all design and layout elements, should not use stock image other than the types specified (hourglass, sofa, loveseat, lamp and bed), should not use images not licensed from stock photo sites

```html
<!DOCTYPE html>
<html lang="en">
<head>
<meta charset="utf-8">
<title>Nestora – Login</title>
<link rel="stylesheet" href="https://fonts.googleapis.com/css2?family=Source+Sans+3:wght@400;600;800&display=swap">
<style>
  :root {
    --ink: #111111;
    --text: #4a4a4a;
    --white: #ffffff;
    --lavender: #b07fd9;
    --teal: #0e9a94;
    --teal-soft: #5fbdb4;
    --plum: #a0136e;
    --peach: #f2b385;
    --sofa-light: #c9c9c9;
    --sofa-dark: #6f6f6f;
    --panel: rgba(240, 240, 240, 0.55);
  }
  * { margin: 0; padding: 0; box-sizing: border-box; }
  html, body { width: 676px; height: 1200px; overflow: hidden; background: var(--white); }
  body { position: relative; font-family: "Source Sans 3", sans-serif; color: var(--text); }

  .top-bar { position: absolute; top: 0; left: 0; width: 676px; height: 90px; }
  .back-button { position: absolute; left: 36px; top: 28px; }
  .brand-name {
    position: absolute; left: 0; right: 0; top: 14px; text-align: center;
    font-weight: 800; font-size: 54px; letter-spacing: -1.5px; color: var(--ink);
  }
  .menu-button { position: absolute; left: 600px; top: 36px; }

  .sofa-visual {
    position: absolute; left: 10px; top: 360px; width: 646px; height: 372px;
    border-radius: 40px 40px 14px 14px;
    background: radial-gradient(ellipse at 50% 45%, var(--sofa-light) 0%, #a9a9a9 60%, var(--sofa-dark) 100%);
  }

  .login-panel {
    position: absolute; left: 47px; top: 377px; width: 580px; height: 315px;
    background: var(--panel); border: 1px solid rgba(255,255,255,0.9); border-radius: 10px;
  }
  .field {
    position: absolute; left: 33px; width: 508px; height: 57px;
    background: var(--white); border-radius: 8px; display: flex; align-items: center;
  }
  .field--user { top: 34px; border-bottom: 2px solid var(--lavender); }
  .field--password { top: 109px; height: 56px; border-bottom: 2px solid var(--teal); }
  .field-icon { width: 56px; display: flex; justify-content: center; }
  .field-divider { width: 1px; height: 34px; background: #777; }
  .field-label { padding-left: 9px; font-size: 20px; color: var(--text); }

  .form-links {
    position: absolute; left: 33px; top: 176px; width: 508px;
    display: flex; justify-content: space-between; font-size: 20px;
  }
  .register-link { color: var(--teal-soft); }
  .forgot-link { color: var(--plum); }

  .login-button {
    position: absolute; left: 34px; top: 220px; width: 506px; height: 48px;
    background: var(--peach); color: var(--white); border-radius: 3px;
    font-size: 22px; font-weight: 600; display: flex; align-items: center; justify-content: center;
  }

  .page-dots { position: absolute; top: 1091px; left: 267px; display: flex; gap: 13px; }
  .page-dot { width: 20px; height: 20px; border-radius: 50%; }
  .dot-lavender { background: var(--lavender); }
  .dot-teal { background: var(--teal); }
  .dot-plum { background: var(--plum); }
  .dot-peach { background: var(--peach); }
</style>
</head>
<body>
  <header class="top-bar">
    <svg class="back-button" width="24" height="34" viewBox="0 0 24 34" aria-label="Back">
      <polyline points="20,3 6,17 20,31" fill="none" stroke="var(--ink)" stroke-width="4"/>
    </svg>
    <div class="brand-name">Nestora</div>
    <svg class="menu-button" width="34" height="20" viewBox="0 0 34 20" aria-label="Menu">
      <line x1="0" y1="2" x2="34" y2="2" stroke="var(--ink)" stroke-width="2"/>
      <line x1="0" y1="10" x2="34" y2="10" stroke="var(--ink)" stroke-width="2"/>
      <line x1="0" y1="18" x2="34" y2="18" stroke="var(--ink)" stroke-width="2"/>
    </svg>
  </header>

  <div class="sofa-visual" role="img" aria-label="Grey textured loveseat photograph"></div>

  <main class="login-panel">
    <div class="field field--user">
      <span class="field-icon">
        <svg width="26" height="28" viewBox="0 0 26 28">
          <circle cx="13" cy="9" r="6.5" fill="none" stroke="var(--lavender)" stroke-width="1.5"/>
          <path d="M2 27 C2 19 7 16 13 16 C19 16 24 19 24 27 Z" fill="none" stroke="var(--lavender)" stroke-width="1.5"/>
        </svg>
      </span>
      <span class="field-divider"></span>
      <span class="field-label">User Name</span>
    </div>
    <div class="field field--password">
      <span class="field-icon">
        <svg width="24" height="28" viewBox="0 0 24 28">
          <path d="M6 12 V8 A6 6 0 0 1 18 8 V12" fill="none" stroke="var(--teal)" stroke-width="1.5"/>
          <rect x="2" y="12" width="20" height="15" rx="3" fill="none" stroke="var(--teal)" stroke-width="1.5"/>
          <text x="12" y="23" font-size="8" text-anchor="middle" fill="var(--teal)" font-family="Source Sans 3, sans-serif">0</text>
        </svg>
      </span>
      <span class="field-divider"></span>
      <span class="field-label">Password</span>
    </div>
    <div class="form-links">
      <span class="register-link">Register now</span>
      <span class="forgot-link">Forgot Password?</span>
    </div>
    <div class="login-button">LOGIN</div>
  </main>

  <nav class="page-dots" aria-label="Pages">
    <span class="page-dot dot-lavender"></span>
    <span class="page-dot dot-teal"></span>
    <span class="page-dot dot-plum"></span>
    <span class="page-dot dot-peach"></span>
    <span class="page-dot dot-teal"></span>
  </nav>
</body>
</html>
```